Aufkleberdesign für 3d Messdienstleistungen
Zielgruppe
3d Messdienstleistungen in Industrie, Architektur und Schiffbau
Aufgabenstellung
technisches Design, ansprechend, rational
Wir benötigen Aufkleber mit sehr kurzen Informationen über unsere Dienstleistung, die wir auf den Messobjekten bei unseren Kunden hinterlassen,
- Logo (vorhanden),
- Kontaktdaten,
- Dienstleistungen (Liste von 4-5 Schlagwörtern), (Kalibrierung von Laserprojektion, Industrievermessung, Kranbahnvermessung, Bauwerksvermessung)
- netter Hintergrund
A4, A5, A6 für Druck, Querformat

```html
<!DOCTYPE html>
<html lang="de">
<head>
<meta charset="utf-8">
<title>Kessler &amp; Brandt – Leistungen</title>
<link rel="stylesheet" href="https://fonts.googleapis.com/css2?family=Lato:wght@700;900&family=Roboto:wght@500&display=swap">
<style>
  :root {
    --ink: #050505;
    --paper: #ffffff;
    --teal: #5fb7c6;
    --teal-deep: #4a9fb0;
    --cube: #7fc7d6;
    --brand-blue: #1b8fd6;
    --scan-orange: #e8501c;
    --scan-yellow: #e9c21a;
    --scan-cyan: #35b8d8;
    --scan-green: #1f3a14;
  }
  * { margin: 0; padding: 0; box-sizing: border-box; }
  html, body { width: 1200px; height: 848px; overflow: hidden; background: var(--paper); }
  .sticker {
    position: relative;
    width: 1200px; height: 848px;
    background: var(--ink);
    overflow: hidden;
    font-family: "Lato", sans-serif;
    color: var(--paper);
  }
  .artwork { position: absolute; inset: 0; }
  .brand {
    position: absolute; left: 110px; top: 74px;
    display: flex; align-items: center; gap: 16px;
  }
  .brand-mark { width: 38px; height: 38px; background: var(--brand-blue); flex: none; }
  .brand-name {
    font-family: "Lato", sans-serif; font-weight: 700;
    font-size: 32px; letter-spacing: 0; color: var(--paper);
  }
  .services { position: absolute; left: 110px; top: 200px; }
  .services-title {
    font-weight: 900; font-size: 58px; letter-spacing: 1px; margin-bottom: 22px;
  }
  .service-list { list-style: none; }
  .service-item {
    display: flex; align-items: flex-start; gap: 18px;
    font-weight: 700; font-size: 36px; line-height: 1.22; margin-bottom: 10px;
  }
  .service-icon { width: 32px; height: 34px; flex: none; margin-top: 6px; }
  .contact {
    position: absolute; left: 60px; top: 665px;
    font-family: "Roboto", sans-serif; font-weight: 500; font-style: normal;
    font-size: 23px; line-height: 1.45; color: var(--paper);
  }
</style>
</head>
<body>
<main class="sticker">
  <svg class="artwork" width="1200" height="848" viewBox="0 0 1200 848" xmlns="http://www.w3.org/2000/svg">
    <defs>
      <linearGradient id="scan-plan" x1="0" y1="0" x2="1" y2="1">
        <stop offset="0" stop-color="var(--scan-green)"/>
        <stop offset="0.35" stop-color="var(--scan-cyan)"/>
        <stop offset="0.7" stop-color="var(--scan-yellow)"/>
        <stop offset="1" stop-color="var(--scan-orange)"/>
      </linearGradient>
      <linearGradient id="scan-view" x1="0" y1="0" x2="1" y2="1">
        <stop offset="0" stop-color="var(--scan-orange)"/>
        <stop offset="0.5" stop-color="var(--scan-yellow)"/>
        <stop offset="1" stop-color="var(--scan-orange)"/>
      </linearGradient>
      <linearGradient id="band" x1="0" y1="0" x2="1" y2="0">
        <stop offset="0" stop-color="var(--teal)"/>
        <stop offset="1" stop-color="var(--teal-deep)"/>
      </linearGradient>
      <linearGradient id="device" x1="0" y1="0" x2="0" y2="1">
        <stop offset="0" stop-color="#dcdcdc"/>
        <stop offset="0.6" stop-color="#b9b9b9"/>
        <stop offset="1" stop-color="#222"/>
      </linearGradient>
    </defs>

    <path d="M590 96 H1200 V486 H590 Z" fill="var(--paper)"/>
    <rect x="606" y="96" width="594" height="376" fill="url(#scan-plan)" role="img" aria-label="Laserscan-Punktwolke einer Kirche in der Draufsicht mit Bäumen"/>

    <path d="M640 518 H1200 V848 H450 Z" fill="var(--paper)"/>
    <path d="M652 532 H1200 V848 H470 Z" fill="url(#scan-view)" role="img" aria-label="Laserscan-Punktwolke einer Kirche in Schrägansicht"/>

    <path d="M0 640 H560 L480 848 H0 Z" fill="url(#band)"/>

    <path d="M890 470 Q890 452 910 452 H1040 Q1060 452 1060 470 V848 H860 V700 Q880 690 880 640 Z" fill="var(--paper)"/>
    <path d="M900 478 Q900 464 914 464 H1036 Q1050 464 1050 478 V848 H872 V706 Q892 694 892 646 Z" fill="url(#device)" role="img" aria-label="Lasertracker auf Stativ"/>
  </svg>

  <div class="brand">
    <span class="brand-mark"></span>
    <span class="brand-name">Kessler &amp; Brandt</span>
  </div>

  <section class="services">
    <h1 class="services-title">LEISTUNGEN:</h1>
    <ul class="service-list">
      <li class="service-item">
        <svg class="service-icon" viewBox="0 0 32 34"><path d="M16 1 L31 9 V25 L16 33 L1 25 V9 Z" fill="var(--cube)"/><path d="M16 17 L31 9 M16 17 L1 9 M16 17 V33" stroke="var(--ink)" stroke-width="1.5" fill="none"/></svg>
        <span>Kalibrierung von<br>Laserprojektion</span>
      </li>
      <li class="service-item">
        <svg class="service-icon" viewBox="0 0 32 34"><path d="M16 1 L31 9 V25 L16 33 L1 25 V9 Z" fill="var(--cube)"/><path d="M16 17 L31 9 M16 17 L1 9 M16 17 V33" stroke="var(--ink)" stroke-width="1.5" fill="none"/></svg>
        <span>Industrievermessung</span>
      </li>
      <li class="service-item">
        <svg class="service-icon" viewBox="0 0 32 34"><path d="M16 1 L31 9 V25 L16 33 L1 25 V9 Z" fill="var(--cube)"/><path d="M16 17 L31 9 M16 17 L1 9 M16 17 V33" stroke="var(--ink)" stroke-width="1.5" fill="none"/></svg>
        <span>Kranbahnvermessung</span>
      </li>
      <li class="service-item">
        <svg class="service-icon" viewBox="0 0 32 34"><path d="M16 1 L31 9 V25 L16 33 L1 25 V9 Z" fill="var(--cube)"/><path d="M16 17 L31 9 M16 17 L1 9 M16 17 V33" stroke="var(--ink)" stroke-width="1.5" fill="none"/></svg>
        <span>Bauwerksvermessung</span>
      </li>
    </ul>
  </section>

  <address class="contact">
    Kessler &amp; Brandt 3d Solutions GmbH<br>
    +49 (0)4105 5530128 | info@kb-3dm.de<br>
    www.kb-3dm.de
  </address>
</main>
</body>
</html>
```